Design for Employee Baseball Cards

Looking to design baseball cards for my employees. Trying to replicate famous baseball card design with swapping in an employee and listing there stats and fun facts. These cards will be inserted into boxes so customers can receive with their orders. Cards allow customers to put a face to the name they've always corresponded with, which makes their experience personable and more memorable.

Looking for a front and back design template. We are open to the design, but would like it to resemble a baseball/playing card.
Size: 2.5" x 3.5" vertical
Here is our website which can be referenced for color pallet and tone.
https://www.crateswithmarlow.com/

Attached is an example of a vintage baseball. Can we see some versions like this?

Front
- Person's name
- Title/Department
- Crates With Marlow logo
- Person's photo - this will be an action shot like a baseball card

Back
I'm open to the design and content of the back. We want it to resemble a back of a baseball card as best as possible. Normally, baseball cards will have stats by year. Instead, we can have stats and fun facts like the following

Items for Back
- Bio
- Year started at CWM
- Department
- Years of experience
- Specialty
- Secret skill
- What you love about CWM
- Favorite quote
- Fun fact
- Passion outside of CWM
- Person's photo - we can include a smaller headshot

Font styles to use
Sans Serif

Colors
0054AA
0677BA
7BADD7
CADEEF
E8F1F8

Requirements
Must have
• The deliverable must be a template PSD or AI that we can swap in photos and edit text for each person's card.

```html
<!DOCTYPE html>
<html lang="en">
<head>
<meta charset="utf-8">
<title>Employee Trading Card – Front and Back Template</title>
<link rel="stylesheet" href="https://fonts.googleapis.com/css2?family=Oswald:wght@500;600;700&family=Open+Sans:wght@400&display=swap">
<style>
  :root {
    --blue-deep: #0054AA;
    --blue-mid: #0677BA;
    --blue-soft: #7BADD7;
    --blue-pale: #CADEEF;
    --blue-mist: #E8F1F8;
    --navy: #0d2a55;
    --ink: #111111;
    --star-grey: #b9b9b9;
    --paper: #ffffff;
  }
  html, body {
    margin: 0;
    padding: 0;
    width: 1200px;
    height: 1200px;
    overflow: hidden;
    background: var(--paper);
  }
  .sheet {
    position: relative;
    width: 1200px;
    height: 1200px;
  }
  .card {
    position: absolute;
    width: 518px;
    height: 725px;
    display: block;
  }
  .card--front { left: 84px; top: 149px; }
  .card--back { left: 626px; top: 347px; }
  .side-label {
    position: absolute;
    margin: 0;
    font-family: "Open Sans", sans-serif;
    font-weight: 400;
    font-size: 64px;
    line-height: 1;
    color: var(--ink);
    transform: translateX(-50%);
    white-space: nowrap;
  }
  .side-label--back { left: 874px; top: 265px; }
  .side-label--front { left: 329px; top: 918px; }

  .bg-deep { fill: var(--blue-deep); }
  .bg-mid { fill: var(--blue-mid); }
  .banner-edge { fill: var(--navy); }
  .banner-face { fill: var(--blue-pale); }
  .frame-outer { fill: var(--blue-mist); }
  .frame-inner { fill: var(--blue-deep); }
  .star { fill: var(--blue-mist); }
  .star--grey { fill: var(--star-grey); }
  .player-name {
    font-family: "Oswald", sans-serif;
    font-weight: 700;
    font-size: 80px;
    fill: var(--blue-deep);
  }
  .player-title {
    font-family: "Oswald", sans-serif;
    font-weight: 600;
    font-size: 38px;
    fill: var(--blue-deep);
  }
  .headshot-ring { fill: var(--navy); }
  .headshot-face { fill: var(--paper); }
  .headshot-label {
    font-family: "Oswald", sans-serif;
    font-weight: 700;
    font-size: 42px;
    fill: var(--ink);
  }
  .stats-frame { fill: var(--blue-deep); }
  .stats-panel { fill: var(--paper); }
  .stat-label {
    font-family: "Oswald", sans-serif;
    font-weight: 600;
    font-size: 35px;
    fill: var(--blue-deep);
  }
  .stat-line { stroke: var(--ink); stroke-width: 5; }
</style>
</head>
<body>
<main class="sheet">

  <p class="side-label side-label--back">BACK</p>
  <p class="side-label side-label--front">FRONT</p>

  <!-- Front of card -->
  <svg class="card card--front" viewBox="0 0 828 1159" xmlns="http://www.w3.org/2000/svg" aria-label="Card front">
    <defs>
      <path id="star-shape" d="M0,-1 L0.225,-0.309 L0.951,-0.309 L0.363,0.118 L0.588,0.809 L0,0.382 L-0.588,0.809 L-0.363,0.118 L-0.951,-0.309 L-0.225,-0.309Z"/>
      <linearGradient id="action-shot-tones" x1="0" y1="0" x2="1" y2="1">
        <stop offset="0" stop-color="#8fb25a"/>
        <stop offset="0.35" stop-color="#b59c7c"/>
        <stop offset="0.7" stop-color="#9a9aa0"/>
        <stop offset="1" stop-color="#a98e72"/>
      </linearGradient>
    </defs>
    <rect class="bg-deep" width="828" height="1159"/>
    <polygon class="bg-mid" points="0,0 430,0 828,430 828,1028 28,1112 0,1112"/>

    <rect class="frame-outer" x="51" y="78" width="726" height="944" rx="10"/>
    <rect class="frame-inner" x="63" y="90" width="702" height="920"/>
    <g role="img" aria-label="Action photo of the employee in a baseball pose">
      <rect x="75" y="102" width="679" height="898" fill="url(#action-shot-tones)"/>
    </g>

    <polygon class="banner-edge" points="0,20 658,20 533,185 0,185"/>
    <polygon class="banner-face" points="0,31 638,31 523,175 0,175"/>
    <text class="player-name" x="287" y="114" text-anchor="middle" textLength="449" lengthAdjust="spacingAndGlyphs">MARCUS BELLWEATHER</text>
    <text class="player-title" x="282" y="157" text-anchor="middle" textLength="180" lengthAdjust="spacing">MANAGER</text>

    <use href="#star-shape" class="star" transform="translate(733 1084) rotate(-6) scale(66)"/>
    <use href="#star-shape" class="star" transform="translate(630 1099) rotate(-6) scale(33)"/>
    <use href="#star-shape" class="star" transform="translate(552 1114) rotate(-6) scale(29)"/>
    <use href="#star-shape" class="star" transform="translate(479 1124) rotate(-6) scale(25)"/>
  </svg>

  <!-- Back of card -->
  <svg class="card card--back" viewBox="0 0 828 1159" xmlns="http://www.w3.org/2000/svg" aria-label="Card back">
    <defs>
      <path id="star-shape-back" d="M0,-1 L0.225,-0.309 L0.951,-0.309 L0.363,0.118 L0.588,0.809 L0,0.382 L-0.588,0.809 L-0.363,0.118 L-0.951,-0.309 L-0.225,-0.309Z"/>
    </defs>
    <rect class="bg-deep" width="828" height="1159"/>
    <polygon class="bg-mid" points="0,0 430,0 828,430 828,1025 29,1108 0,1108"/>
    <polygon class="bg-deep" points="0,210 560,250 0,282"/>

    <rect class="stats-frame" x="41" y="333" width="755" height="692"/>
    <rect class="stats-panel" x="59" y="296" width="725" height="709"/>

    <text class="stat-label" x="78" y="358">Bio</text>
    <line class="stat-line" x1="150" y1="360" x2="751" y2="360"/>
    <text class="stat-label" x="78" y="446">Year started at CWM</text>
    <line class="stat-line" x1="380" y1="444" x2="751" y2="444"/>
    <text class="stat-label" x="78" y="534">Department</text>
    <line class="stat-line" x1="282" y1="537" x2="751" y2="537"/>
    <text class="stat-label" x="78" y="622">Years of experience</text>
    <line class="stat-line" x1="397" y1="622" x2="751" y2="622"/>

    <use href="#star-shape-back" class="star--grey" transform="translate(359 685) rotate(-6) scale(46)"/>
    <use href="#star-shape-back" class="star--grey" transform="translate(435 690) rotate(-6) scale(21)"/>
    <use href="#star-shape-back" class="star--grey" transform="translate(491 697) rotate(-6) scale(18)"/>
    <use href="#star-shape-back" class="star--grey" transform="translate(544 703) rotate(-6) scale(14)"/>

    <text class="stat-label" x="78" y="755">Specialty</text>
    <line class="stat-line" x1="261" y1="756" x2="749" y2="756"/>
    <text class="stat-label" x="78" y="799">Secret skill</text>
    <line class="stat-line" x1="263" y1="799" x2="749" y2="799"/>
    <text class="stat-label" x="78" y="843">What you love about CWM</text>
    <line class="stat-line" x1="454" y1="845" x2="749" y2="845"/>
    <text class="stat-label" x="78" y="887">Favorite quote</text>
    <line class="stat-line" x1="305" y1="890" x2="749" y2="890"/>
    <text class="stat-label" x="78" y="932">Fun fact</text>
    <line class="stat-line" x1="212" y1="933" x2="749" y2="933"/>
    <text class="stat-label" x="78" y="975">Passion outside of CWM</text>
    <line class="stat-line" x1="446" y1="979" x2="749" y2="979"/>

    <polygon class="banner-edge" points="0,20 658,20 533,185 0,185"/>
    <polygon class="banner-face" points="0,31 638,31 523,175 0,175"/>
    <text class="player-name" x="287" y="114" text-anchor="middle" textLength="449" lengthAdjust="spacingAndGlyphs">MARCUS BELLWEATHER</text>
    <text class="player-title" x="282" y="157" text-anchor="middle" textLength="180" lengthAdjust="spacing">MANAGER</text>

    <circle class="headshot-ring" cx="659" cy="195" r="143"/>
    <circle class="headshot-face" cx="659" cy="195" r="131"/>
    <text class="headshot-label" x="655" y="197" text-anchor="middle">PERSON</text>
    <text class="headshot-label" x="652" y="243" text-anchor="middle">PHOTO</text>

    <use href="#star-shape-back" class="star" transform="translate(724 1085) rotate(-6) scale(68)"/>
    <use href="#star-shape-back" class="star" transform="translate(633 1095) rotate(-6) scale(33)"/>
    <use href="#star-shape-back" class="star" transform="translate(551 1110) rotate(-6) scale(29)"/>
    <use href="#star-shape-back" class="star" transform="translate(480 1124) rotate(-6) scale(25)"/>
  </svg>

</main>
</body>
</html>
```